Flier Template in Microsoft Word

We need to a have a flier about farm practices developed in Microsoft Word. Each farm will able to add their own logos and photos. We will give them a model that they can customize.

We want a traditional "country" flavor. Green colors and earth tones are best. Please use the photos we have provided.

The final product must be in Microsoft Word for our farmers to customize.
Updates

All designers: Please have a white background (maybe with a watermark). Our client will print these on white paper using a desktop printer. Thank you!

Target Market(s)

People who shop at Farmer's Markets, join CSAs, and enjoy cooking with fresh vegetables.

Industry/Entity Type

Farm

Font styles to use
Serif

Requirements
Must have
• Must use the text and general layout of the Microsoft Word document attached
Must use the pictures we provided.
Final product must be in Microsoft Word
Must be able to easily swap out the logo at the top
Must be able to print on white paper on a desktop printer
Nice to have
• A nice header that looks like a farm or food on the table
A nice watermark or background to make the flier look polished
Should not have
• Do not change the photos
Do not use high tech fonts or graphic treatments

```html
<!DOCTYPE html>
<html lang="en">
<head>
<meta charset="utf-8">
<title>Sustainable Grazing – Maple Hollow Dairy Farm</title>
<link href="https://fonts.googleapis.com/css2?family=Roboto:wght@400;500;700&family=Tinos:wght@700&display=swap" rel="stylesheet">
<style>
  :root {
    --leaf-deep: #1f8a2a;
    --leaf-bright: #6cc43a;
    --heading-green: #1f6b2c;
    --body-ink: #2a2a2a;
    --paper: #ffffff;
    --grass-dark: #3f8f1e;
    --grass-light: #b7e07a;
    --badge-green: #c9ec9a;
  }
  * { margin: 0; padding: 0; box-sizing: border-box; }
  html, body { width: 927px; height: 1200px; overflow: hidden; background: var(--paper); }
  .flier {
    position: relative; width: 927px; height: 1200px; background: var(--paper);
    font-family: "Roboto", Arial, sans-serif; color: var(--body-ink);
  }
  .masthead {
    position: absolute; left: 0; top: 0; width: 927px; height: 140px;
    background: linear-gradient(100deg, var(--leaf-deep) 0%, #3fa82e 45%, var(--leaf-bright) 75%, #2d9a2b 100%);
  }
  .logo-slot {
    position: absolute; left: 30px; top: 56px;
    font-family: "Tinos", "Times New Roman", serif; font-weight: 700;
    font-size: 27px; color: #ffffff; letter-spacing: 0.5px;
  }
  .page-title {
    position: absolute; left: 39px; top: 162px;
    font-size: 29px; font-weight: 500; color: var(--heading-green);
  }
  .section { position: absolute; left: 39px; width: 849px; }
  .section h2 { font-size: 25px; font-weight: 500; color: var(--heading-green); margin-bottom: 6px; }
  .section p { font-size: 16.3px; text-align: justify; }
  .who { top: 228px; width: 567px; }
  .who p { line-height: 30.5px; }
  .done { top: 426px; }
  .done p { line-height: 27.8px; }
  .when { top: 630px; }
  .when p { line-height: 33px; }
  .photo { position: absolute; }
  .photo-farmer { left: 636px; top: 235px; width: 258px; height: 166px;
    background: linear-gradient(180deg, #e4ece6 0%, #9fb98a 45%, #5f8f3a 100%); }
  .photo-pasture { left: 101px; top: 827px; width: 335px; height: 215px;
    background: linear-gradient(180deg, #dfe8ee 0%, #8e9a78 30%, #8aa24e 60%, #6d7a44 100%); }
  .photo-stream { left: 497px; top: 827px; width: 335px; height: 215px;
    background: linear-gradient(180deg, #e3edf3 0%, #93a07c 30%, #7fa04a 60%, #6a8234 100%); }
  .grass-band {
    position: absolute; left: 0; top: 1083px; width: 927px; height: 117px;
    background: linear-gradient(180deg, rgba(255,255,255,0) 0%, var(--grass-light) 30%, var(--grass-dark) 100%);
  }
  .partner-badge {
    position: absolute; left: 757px; top: 1091px; width: 143px; height: 109px;
    background: #ffffff;
  }
</style>
</head>
<body>
<div class="flier">
  <header class="masthead">
    <div class="logo-slot">LOGO HERE</div>
  </header>

  <h1 class="page-title">Sustainable Grazing</h1>

  <section class="section who">
    <h2>Who We Are</h2>
    <p>Maple Hollow Dairy Farm is a third generation dairy farm located on 64 acres in the Willow Creek Valley. We raise holsteins to produce milk and also raise hens for eggs. We sell much of our milk, as well as cheese, yogurt and baked goods directly from the farm.</p>
  </section>
  <div class="photo photo-farmer" role="img" aria-label="Farmer standing with arms crossed in front of a red tractor in a green field"></div>

  <section class="section done">
    <h2>What Have We Done</h2>
    <p>At Maple Hollow Dairy Farm, we take care of our animals and our animals help us take care of the land. Corn and other grains are not a natural part of a cows’ diet, so we don’t feed them that. Instead, we let them roam the pastures eating grass and other plants. We move the cows from pasture to pasture on a thoughtful schedule to prevent overgrazing, and this reduces soil erosion and water pollution. Our animals are happier and our land and water is healthier.</p>
  </section>

  <section class="section when">
    <h2>When and Where We Did It</h2>
    <p>In 2010, we had our cows in a stall barn and corn or soybeans in our fields. We looked into switching some of our acreage from crops to pasture and soon realized that it would beneficial to our cows and our soil. We then installed fencing to divide the fields into smaller paddocks and in spring 2011, we planted a seed mixture containing plants that provide the nutrition our cows need and that provides support for the soil.</p>
  </section>

  <div class="photo photo-pasture" role="img" aria-label="Cattle grazing in a pasture beside a small stream with hills behind"></div>
  <div class="photo photo-stream" role="img" aria-label="Fenced stream corridor with tall grass running through a pasture"></div>

  <div class="grass-band" role="img" aria-label="Band of green grass along the bottom of the page"></div>
  <div class="partner-badge">
    <svg width="143" height="109" viewBox="0 0 143 109" aria-hidden="true">
      <circle cx="78" cy="52" r="42" fill="var(--badge-green)"/>
    </svg>
  </div>
</div>
</body>
</html>
```